Website - Tides Of Bloom

We are catalysts of change in people's lives.
We work with individuals and professionals to bring about instant substantial & transforming change in their lives.
We provide one-on-one lifestyle coaching by an experienced practitioner.
Our existing website is www.tidesofbloom.biz & this site contains our the basis for the content of our desired new project, so please examine this carefully.
We require a professional and captivating website that will instantly impress, engage invite our readers to click & invest their lives.
Our services do not come cheap, but are second to none.
Our website must be contemporary whilst reflecting indisputable class & ultra-confidence in the success of our work.
Target Market(s)
Those who seek to want to change in their lives. Those aged primarily between 30 and 50 years of age, male or female.
Industry/Entity Type
Work
Look and feel

```html
<!DOCTYPE html>
<html lang="en">
<head>
<meta charset="utf-8">
<title>Tides Of Bloom</title>
<link href="https://fonts.googleapis.com/css2?family=Arimo:wght@400;700&family=Open+Sans:wght@400;600&display=swap" rel="stylesheet">
<style>
  :root {
    --black: #000000;
    --orange: #f07a1e;
    --orange-text: #ee6f1f;
    --white: #ffffff;
    --text: #555555;
    --muted: #777777;
    --line: #d6d6d6;
    --footer: #434343;
    --link-blue: #1f7fc4;
    --logo-grey: #b9b9b9;
  }
  * { box-sizing: border-box; margin: 0; padding: 0; }
  html, body { width: 972px; height: 1200px; overflow: hidden; background: var(--white); }
  body { position: relative; font-family: "Arimo", Arial, sans-serif; color: var(--text); }

  .site-header { position: absolute; left: 0; top: 0; width: 972px; height: 106px; background: var(--black); }
  .brand { position: absolute; left: 88px; top: 24px; display: flex; align-items: center; gap: 10px; }
  .brand-mark { width: 52px; height: 52px; background: var(--logo-grey); }
  .brand-name { font-size: 26px; line-height: 28px; font-weight: 400; color: var(--logo-grey); width: 120px; }

  .main-nav { position: absolute; left: 350px; top: 40px; display: flex; align-items: center; }
  .main-nav a { color: var(--white); text-decoration: none; font-size: 14px; height: 28px; line-height: 28px; }
  .main-nav .current { background: var(--orange); padding: 0 17px; border-radius: 2px; margin-right: 22px; }
  .main-nav .item { margin-right: 42px; }

  .search { position: absolute; left: 716px; top: 41px; width: 164px; height: 24px; background: var(--white); border: 1px solid #ccc; }
  .search span { position: absolute; left: 10px; top: 5px; font-size: 12px; color: #777; }
  .search svg { position: absolute; right: 8px; top: 6px; }

  .hero { position: absolute; left: 0; top: 106px; width: 972px; height: 417px;
    background: radial-gradient(ellipse 260px 300px at 420px 230px, #e2ddd8 0%, #eeeeee 55%, #f7f7f7 100%); }
  .hero-arrow { position: absolute; top: 168px; }
  .hero-arrow.prev { left: 70px; }
  .hero-arrow.next { left: 884px; }
  .hero-caption { position: absolute; left: 69px; top: 326px; width: 653px; height: 59px; background: rgba(70,70,70,0.85);
    color: var(--white); font-weight: 700; font-size: 23px; line-height: 59px; padding-left: 18px; letter-spacing: 0.2px; }

  .services { position: absolute; left: 69px; top: 567px; display: flex; gap: 41px; }
  .service-card { width: 250px; height: 233px; background: var(--white); border: 1px solid #e3e3e3; box-shadow: 0 0 4px rgba(0,0,0,0.12); padding: 7px; }
  .service-photo { width: 236px; height: 120px; }
  .service-card h3 { font-weight: 400; font-size: 15px; color: var(--orange-text); margin: 16px 0 6px 3px; }
  .service-card p { font-size: 11.3px; line-height: 17.5px; color: var(--text); margin-left: 3px; }

  .welcome { position: absolute; left: 69px; top: 849px; width: 392px; }
  .welcome h2 { font-weight: 400; font-size: 15px; color: var(--orange-text); margin-bottom: 16px; }
  .welcome p { font-size: 11.6px; line-height: 21.4px; color: var(--text); }

  .testimonials { position: absolute; left: 494px; top: 846px; width: 408px; height: 204px; border: 1px solid #cfcfcf; padding: 19px 29px; }
  .testimonials h2 { font-size: 16px; font-weight: 700; color: #666; margin-bottom: 14px; }
  .quote { position: relative; padding-left: 37px; width: 340px; font-size: 10.8px; line-height: 20.4px; color: var(--muted); }
  .quote .mark { position: absolute; font-family: Georgia, serif; font-size: 44px; color: #c8c8c8; line-height: 1; }
  .quote .open { left: 0; top: -2px; }
  .quote .close { right: -20px; bottom: -24px; }
  .author { position: absolute; left: 34px; top: 140px; display: flex; align-items: center; }
  .author-photo { width: 46px; height: 46px; border-radius: 50%; background: #4a4a4a; }
  .author-info { margin-left: 14px; font-family: "Open Sans", sans-serif; font-size: 12px; }
  .author-info .name { color: #555; }
  .author-info .company { color: var(--link-blue); margin-top: 3px; }
  .dots { position: absolute; right: 40px; top: 169px; display: flex; gap: 4px; }
  .dots i { width: 6px; height: 6px; border-radius: 50%; background: #888; display: block; }
  .dots i.active { background: var(--white); border: 1px solid #888; }

  .site-footer { position: absolute; left: 0; top: 1092px; width: 972px; height: 108px; background: var(--footer);
    font-family: "Open Sans", sans-serif; color: var(--white); font-size: 11px; }
  .legal { position: absolute; left: 72px; top: 32px; line-height: 28px; }
  .social { position: absolute; left: 716px; top: 40px; display: flex; gap: 10px; }
  .social span { width: 30px; height: 30px; display: block; }
  .social .s1 { background: #3b5ea8; }
  .social .s2 { background: #2a9fd8; }
  .social .s3 { background: #f07a1e; }
  .social .s4 { background: #d8262b; }
</style>
</head>
<body>
  <header class="site-header">
    <div class="brand">
      <span class="brand-mark"></span>
      <span class="brand-name">Tides Of Bloom</span>
    </div>
    <nav class="main-nav">
      <a class="current" href="#">Home</a>
      <a class="item" href="#">Business</a>
      <a class="item" href="#">Individual</a>
      <a class="item" href="#">Contact</a>
    </nav>
    <div class="search">
      <span>Search..</span>
      <svg width="12" height="12" viewBox="0 0 12 12"><circle cx="5" cy="5" r="3.6" fill="none" stroke="#999" stroke-width="1.6"/><line x1="7.6" y1="7.6" x2="11" y2="11" stroke="#999" stroke-width="1.8"/></svg>
    </div>
  </header>

  <section class="hero" role="img" aria-label="Smiling businessman in a white shirt and striped tie, seated in a bright blurred meeting room">
    <svg class="hero-arrow prev" width="18" height="50" viewBox="0 0 18 50"><polyline points="16,2 3,25 16,48" fill="none" stroke="#8a8a8a" stroke-width="2"/></svg>
    <svg class="hero-arrow next" width="18" height="50" viewBox="0 0 18 50"><polyline points="2,2 15,25 2,48" fill="none" stroke="#8a8a8a" stroke-width="2"/></svg>
    <div class="hero-caption">WE ARE CATALYSTS OF CHANGE IN PEOPLE'S LIVES.</div>
  </section>

  <section class="services">
    <article class="service-card">
      <div class="service-photo" role="img" aria-label="Two smiling couples in white clothes outdoors" style="background: linear-gradient(180deg,#e8ece0 0%,#d9d4c8 60%,#a9c07a 100%);"></div>
      <h3>One-on-one lifestyle coaching</h3>
      <p>Claritas est etiam processus dynamicus, qui sequitur mutationem consuetudium lectorum. Mirum est notare quam littera gothica, quam.</p>
    </article>
    <article class="service-card">
      <div class="service-photo" role="img" aria-label="Group of laughing young friends lying head to head" style="background: linear-gradient(135deg,#6f97b8 0%,#c9a089 50%,#7f5b45 100%);"></div>
      <h3>Individuals</h3>
      <p>Claritas est etiam processus dynamicus, qui sequitur mutationem consuetudium lectorum. Mirum est notare quam littera gothica, quam.</p>
    </article>
    <article class="service-card">
      <div class="service-photo" role="img" aria-label="Cheerful senior people giving thumbs up" style="background: linear-gradient(135deg,#b9b3ac 0%,#d9c2b0 50%,#9f8f86 100%);"></div>
      <h3>Business</h3>
      <p>Claritas est etiam processus dynamicus, qui sequitur mutationem consuetudium lectorum. Mirum est notare quam littera gothica, quam.</p>
    </article>
  </section>

  <section class="welcome">
    <h2>WELCOME TO OUR WEBSITE</h2>
    <p>Duis autem vel eum iriure dolor in hendrerit in vulputate velit esse molestie consequat, vel illum dolore eu feugiat nulla facilisis at vero eros et accumsan et iusto odio dignissim qui blandit praesent luptatum zzril delenit augue duis dolore te feugait nulla facilisi. Nam liber tempor cum soluta nobis eleifend option congue nihil imperdiet doming id quod mazim placerat facer possimassum. Typi non habent claritatem insitam; est usus legentis in iis qui facit eorum claritatem. Investigationes demonstraverunt lectores legere me lius quod ii legunt saepius.</p>
  </section>

  <section class="testimonials">
    <h2>Testimonials</h2>
    <blockquote class="quote">
      <span class="mark open">&ldquo;</span>
      Maecenas sit amet tincidunt elit. Pellentesque habitaque sene ctuset netus et malesuada fams ac turpisiegeistas. Nulla facilisi. Pellentesque habitant morbi tristique.
      <span class="mark close">&rdquo;</span>
    </blockquote>
    <div class="author">
      <div class="author-photo" role="img" aria-label="Portrait of the client"></div>
      <div class="author-info">
        <div class="name">Daniel Marsh</div>
        <div class="company">Company Name</div>
      </div>
    </div>
    <div class="dots"><i class="active"></i><i></i><i></i><i></i></div>
  </section>

  <footer class="site-footer">
    <div class="legal">
      <div>Privacy Policy | Terms and Conditions</div>
      <div>Copyrights 2013. All Rights Reserved.</div>
    </div>
    <div class="social">
      <span class="s1"></span><span class="s2"></span><span class="s3"></span><span class="s4"></span>
    </div>
  </footer>
</body>
</html>
```